Banner for promote service of debit card

We are PagaVelo and we need the banners to be posted on the facebook and instagram pages.
We want something to communicate that it is an exclusive debit card full of services.
Low commissions.
Our competitors:
https://www.nortapay-pagos.it/it/home.html
https://www.zelkor-conti.it/it/
https://www.fotoreelz.it/serravanbank/
sendquillo
maybe some banner that makes the idea of a convenient debit card that everyone can use.
Girls enjoying card shopping.
Please check also website for slogans and phrases to use
https://www.pagavelo-carta.it/
Should show the services.
We must convey that it is a fast, simple card that guarantees privacy.
We need strong banners that attract people as these ban will be sponsored on instagram and facebook
Target Market(s)
People 18-35 y
Open Bank account. low commissions. Easy to use. No limits. 100% Privacy.
Requirements
Must have
- Written in Italian.

```html
<!DOCTYPE html>
<html lang="it">
<head>
<meta charset="utf-8">
<title>PagaVelo – Una carta per tutti</title>
<link rel="stylesheet" href="https://fonts.googleapis.com/css2?family=Montserrat:wght@500;600;700;800&display=swap">
<style>
  :root {
    --magenta: #a9178f;
    --fuchsia: #d4206f;
    --red: #ef3b3b;
    --ring: #f0503a;
    --white: #ffffff;
    --yellow: #f8d66c;
    --logo-grey: #5a5a5a;
    --photo-light: #f1ede9;
    --photo-warm: #d9c3ae;
  }
  html, body {
    margin: 0;
    padding: 0;
    overflow: hidden;
    background: #ffffff;
  }
  .banner {
    position: relative;
    width: 1200px;
    height: 457px;
    overflow: hidden;
    font-family: "Montserrat", sans-serif;
    color: var(--white);
  }
  .banner-bg {
    position: absolute;
    inset: 0;
    width: 1200px;
    height: 457px;
  }
  .brand-badge {
    position: absolute;
    left: 505px;
    top: 120px;
    width: 214px;
    height: 214px;
    box-sizing: border-box;
    border-radius: 50%;
    background: var(--white);
    border: 10px solid var(--ring);
    display: flex;
    flex-direction: column;
    align-items: center;
    justify-content: center;
    gap: 14px;
  }
  .brand-dot {
    width: 34px;
    height: 34px;
    border-radius: 50%;
    background: var(--ring);
  }
  .brand-name {
    font-weight: 700;
    font-size: 27px;
    color: var(--logo-grey);
    letter-spacing: 0.2px;
  }
  .copy {
    position: absolute;
    left: 786px;
    top: 46px;
    width: 400px;
  }
  .headline {
    margin: 0;
    font-weight: 800;
    font-size: 38px;
    line-height: 46px;
  }
  .subheadline {
    margin: 0 0 14px;
    font-weight: 700;
    font-size: 31px;
    line-height: 40px;
  }
  .features {
    margin: 0 0 26px;
    font-weight: 500;
    font-size: 21px;
    line-height: 32px;
  }
  .promise {
    margin: 0 0 8px;
    font-weight: 700;
    font-size: 24px;
    line-height: 32px;
    color: var(--yellow);
  }
  .promise-note {
    margin: 0;
    font-weight: 700;
    font-size: 17px;
    line-height: 25px;
    color: var(--yellow);
  }
</style>
</head>
<body>
<div class="banner">
  <svg class="banner-bg" viewBox="0 0 1200 457" xmlns="http://www.w3.org/2000/svg">
    <defs>
      <linearGradient id="brandGradient" x1="0" y1="0" x2="1" y2="0">
        <stop offset="0.4" stop-color="#a9178f"/>
        <stop offset="0.7" stop-color="#d4206f"/>
        <stop offset="1" stop-color="#ef3b3b"/>
      </linearGradient>
      <linearGradient id="photoGradient" x1="0" y1="0" x2="1" y2="1">
        <stop offset="0" stop-color="#f1ede9"/>
        <stop offset="0.6" stop-color="#e6d8cb"/>
        <stop offset="1" stop-color="#d9c3ae"/>
      </linearGradient>
    </defs>
    <rect width="1200" height="457" fill="url(#brandGradient)"/>
    <path class="photo-area" role="img"
          aria-label="Foto: ragazza sorridente sdraiata sul letto con carta di debito in mano e laptop davanti"
          d="M0 0 H520 Q650 228 520 457 H0 Z"
          fill="url(#photoGradient)" stroke="#f0503a" stroke-width="8"/>
  </svg>

  <div class="brand-badge">
    <span class="brand-dot"></span>
    <span class="brand-name">PagaVelo</span>
  </div>

  <div class="copy">
    <h1 class="headline">All in One!</h1>
    <h2 class="subheadline">Una carta per tutti</h2>
    <p class="features">Enjoy your cart!<br>Fai quello che vuoi.<br>Nessun limite.<br>Nessun controllo.</p>
    <p class="promise">Privacy garantia.<br>Credito assicurato.</p>
    <p class="promise-note">Usala come vuoi.<br>Senza essere controllato</p>
  </div>
</div>
</body>
</html>
```